Suitor Prediction Show Graphic

I need a graphic for that looks like a fancy spread sheet for a predictions game for a reality show. I want there to be 3 columns, 1:Player A, 2: Question, 3: Player B. There should be at least 10 rows. I am looking for a photoshop template that I can customize later. I have attached the graphic needed for the name of the shows as well as a very basic version of what I am looking for. Please let me know if you need additional information. It should be themed with roses and wedding rings.
SIZE:
1080px by 1920px

Font styles to use
Decorative

Colors
ec1f27
9bcb3c

Requirements
Must have
• The logo for Quelvo and Tindrel. 1080px by 1920px in size.
Nice to have
• Would be nice to have rose vines as the dividers

```html
<!DOCTYPE html>
<html lang="en">
<head>
<meta charset="utf-8">
<title>Quelvo Picks – Tindrel Prediction Sheet</title>
<link rel="stylesheet" href="https://fonts.googleapis.com/css2?family=Berkshire+Swash&family=Cinzel:wght@700&display=swap">
<style>
  :root {
    --paper: #fbf8f1;
    --marble-gold: #e9dcbc;
    --marble-soft: #f3ead6;
    --frame-brown: #6e4c30;
    --header-brown: #5b3a22;
    --header-text: #f6ead2;
    --title-brown: #6a4a2c;
    --grid-line: #7a5638;
    --brand-red: #ec1f27;
    --brand-green: #9bcb3c;
    --ring-gold: #d9b65c;
  }
  * { margin: 0; padding: 0; box-sizing: border-box; }
  html, body { width: 675px; height: 1200px; overflow: hidden; background: var(--paper); }
  .sheet {
    position: relative; width: 675px; height: 1200px; overflow: hidden;
    background: var(--paper);
  }
  .marble-backdrop {
    position: absolute; inset: 0;
    background:
      radial-gradient(ellipse 420px 260px at 85% 12%, var(--marble-gold) 0%, transparent 70%),
      radial-gradient(ellipse 380px 300px at 10% 55%, var(--marble-soft) 0%, transparent 70%),
      radial-gradient(ellipse 460px 280px at 80% 90%, var(--marble-gold) 0%, transparent 70%),
      var(--paper);
    opacity: .85;
  }
  .frame {
    position: absolute; left: 27px; top: 22px; width: 621px; height: 1156px;
    border: 2px solid var(--frame-brown);
  }
  .ornament {
    position: absolute; border-radius: 40%;
    background: radial-gradient(circle, #d8c291 0%, rgba(216,194,145,0) 70%);
    opacity: .7;
  }
  .ornament--top-left { left: 18px; top: 14px; width: 120px; height: 110px; }
  .ornament--bottom-right { right: 18px; bottom: 14px; width: 140px; height: 120px; }
  .ornament--bottom-left { left: 40px; bottom: 40px; width: 70px; height: 60px; }
  .ornament--title-left { left: 130px; top: 196px; width: 60px; height: 34px; }
  .ornament--title-right { right: 130px; top: 196px; width: 60px; height: 34px; }

  .brand-row {
    position: absolute; top: 40px; left: 0; width: 100%;
    display: flex; justify-content: center; align-items: center; gap: 40px;
  }
  .brand-name {
    font-family: "Cinzel", serif; font-weight: 700; font-size: 44px;
    color: var(--brand-red); letter-spacing: 1px;
  }
  .partner-brand { display: flex; align-items: center; gap: 10px; }
  .partner-brand__mark { width: 26px; height: 26px; background: var(--brand-green); }
  .partner-brand__name {
    font-family: "Cinzel", serif; font-weight: 700; font-size: 30px;
    color: var(--brand-red);
  }

  .game-title {
    position: absolute; top: 182px; width: 100%; text-align: center;
    font-family: "Berkshire Swash", cursive; font-size: 44px; color: var(--title-brown);
  }
  .players {
    position: absolute; top: 243px; left: 0; width: 100%; height: 84px;
  }
  .player-name {
    position: absolute; top: 16px;
    font-family: "Berkshire Swash", cursive; font-size: 40px; color: var(--title-brown);
  }
  .player-name--a { left: 170px; }
  .player-name--b { left: 452px; }
  .rings-art {
    position: absolute; left: 265px; top: 0; width: 151px; height: 84px;
    border-radius: 42px;
    background: radial-gradient(ellipse at 40% 50%, #f1dc96 0%, var(--ring-gold) 55%, rgba(217,182,92,0) 100%);
  }

  .picks-table {
    position: absolute; left: 74px; top: 387px; width: 525px;
    border-collapse: collapse; table-layout: fixed;
  }
  .picks-table col.col-answer { width: 167px; }
  .picks-table col.col-question { width: 191px; }
  .picks-table th {
    height: 56px; background: var(--header-brown); color: var(--header-text);
    font-family: "Berkshire Swash", cursive; font-weight: 400; font-size: 30px;
    border-left: 2px solid var(--header-text);
  }
  .picks-table th:first-child { border-left: none; border-top-left-radius: 18px; }
  .picks-table th:last-child { border-top-right-radius: 18px; }
  .picks-table td {
    height: 62px; border: 2px solid var(--grid-line);
    background: rgba(255,255,255,.25);
  }
</style>
</head>
<body>
<main class="sheet">
  <div class="marble-backdrop" role="img" aria-label="Soft cream and gold marble swirl background"></div>
  <div class="frame"></div>

  <div class="ornament ornament--top-left" role="img" aria-label="Gold leaf vine ornament"></div>
  <div class="ornament ornament--bottom-right" role="img" aria-label="Gold leaf vine ornament"></div>
  <div class="ornament ornament--bottom-left" role="img" aria-label="Small gold leaf ornament"></div>
  <div class="ornament ornament--title-left" role="img" aria-label="Small gold leaf flourish"></div>
  <div class="ornament ornament--title-right" role="img" aria-label="Small gold leaf flourish"></div>

  <header class="brand-row">
    <span class="brand-name">Tindrel</span>
    <span class="partner-brand">
      <span class="partner-brand__mark"></span>
      <span class="partner-brand__name">Quelvo</span>
    </span>
  </header>

  <h1 class="game-title">Quelvo Picks</h1>

  <div class="players">
    <span class="player-name player-name--a">Sam</span>
    <div class="rings-art" role="img" aria-label="Pair of interlocked gold wedding rings"></div>
    <span class="player-name player-name--b">JD</span>
  </div>

  <table class="picks-table">
    <colgroup>
      <col class="col-answer"><col class="col-question"><col class="col-answer">
    </colgroup>
    <thead>
      <tr><th>Answer</th><th>Question</th><th>Answer</th></tr>
    </thead>
    <tbody>
      <tr><td></td><td></td><td></td></tr>
      <tr><td></td><td></td><td></td></tr>
      <tr><td></td><td></td><td></td></tr>
      <tr><td></td><td></td><td></td></tr>
      <tr><td></td><td></td><td></td></tr>
      <tr><td></td><td></td><td></td></tr>
      <tr><td></td><td></td><td></td></tr>
      <tr><td></td><td></td><td></td></tr>
      <tr><td></td><td></td><td></td></tr>
      <tr><td></td><td></td><td></td></tr>
      <tr><td></td><td></td><td></td></tr>
    </tbody>
  </table>
</main>
</body>
</html>
```